Medical group practice

We need a flyer design incorporating the three doctors in the practice, there is a general practitioner, ophthalmologist and an obstetrician & Gynaecologist. see the attached file for the concept. will leave the colour design up to you

Target Market(s)

general public

Industry/Entity Type

Health Care

Colors

Designer to choose colors to be used in the design.

Requirements
Must have
• logos included in attachement

```html
<!DOCTYPE html>
<html lang="en">
<head>
<meta charset="utf-8">
<title>Crestview Medical Flyer</title>
<link rel="stylesheet" href="https://fonts.googleapis.com/css2?family=Ubuntu:wght@400;500;700&family=Fredoka:wght@600&family=Oswald:wght@500;600&family=Arimo&display=swap">
<style>
:root{
  --canvas:#000;
  --brand-red:#c8202b;
  --text-grey:#4a4a4a;
  --bar-grey:#5c5c5c;
  --gp-blue:#0070a8;
  --eye-purple:#82067f;
  --obgyn-navy:#0d3a6e;
  --highlight:#ffe600;
  --cream:#f5ead3;
  --ink:#222;
  --gp-name:#0a72a8;
  --ob-name:#0d3f78;
  --green:#009a3a;
}
*{margin:0;padding:0;box-sizing:border-box}
html,body{width:1165px;height:1200px;overflow:hidden;background:var(--canvas)}
.size-label{position:absolute;left:251px;top:71px;color:#fff;font:15px Arimo,sans-serif}
.flyer{position:absolute;left:253px;top:93px;width:659px;height:1019px;background:#fff;overflow:hidden}
.header{position:relative;height:270px;background:linear-gradient(100deg,#f3f5f7 0%,#e9eef2 60%,#dfe7ec 100%)}
.header-photo{position:absolute;right:0;top:0;width:220px;height:270px;
  background:linear-gradient(90deg,rgba(233,238,242,0) 0%,#cfdde6 30%,#b9cfdc 60%,#9fbccc 100%)}
.brand{position:absolute;left:36px;top:104px;display:flex;align-items:center;gap:10px}
.brand-dot{width:22px;height:22px;border-radius:50%;background:var(--brand-red)}
.brand-name{font:700 33px Ubuntu,sans-serif;color:var(--brand-red);letter-spacing:.3px}
.tagline{position:absolute;left:90px;top:145px;font:400 24px Ubuntu,sans-serif;color:var(--text-grey);letter-spacing:.4px}
.address{position:absolute;left:40px;top:176px;width:382px;height:20px;background:var(--bar-grey);
  color:#fff;font:500 14px Oswald,sans-serif;text-align:center;line-height:20px;letter-spacing:.2px}
.specialties{display:flex;gap:3px;height:108px}
.specialty{flex:1;display:flex;flex-direction:column;align-items:center;justify-content:center;text-align:center;color:#fff}
.specialty.gp{background:var(--gp-blue)}
.specialty.eye{background:var(--eye-purple)}
.specialty.obgyn{background:var(--obgyn-navy)}
.specialty h2{font:600 21px/19px Fredoka,sans-serif;color:var(--highlight);margin-bottom:6px}
.phone{font:700 15px/19px Ubuntu,sans-serif;display:flex;align-items:flex-start;gap:4px}
.phone svg{width:14px;height:14px;margin-top:2px;flex:none}
.doctor{position:relative;height:192px;background:linear-gradient(180deg,var(--cream) 0%,#fbf7ef 45%,#fff 100%)}
.doctor-mark{position:absolute;left:72px;top:50%;transform:translateY(-50%);width:100px;height:100px;border-radius:50%}
.doctor.obgyn .doctor-mark{background:#1c4e86}
.doctor.gp .doctor-mark{background:#2a8fb0}
.doctor.eye .doctor-mark{background:#7a2a82}
.doctor-info{position:absolute;left:208px;top:34px}
.doctor.gp .doctor-info{left:204px;top:42px}
.doctor.eye .doctor-info{top:28px}
.doctor-name{font:700 35px/44px Ubuntu,sans-serif}
.doctor.obgyn .doctor-name{color:var(--ob-name)}
.doctor.gp .doctor-name{color:var(--gp-name)}
.doctor.eye .doctor-name{color:var(--eye-purple);line-height:40px}
.service{font:600 33px/38px Oswald,sans-serif;color:var(--ink);transform:scaleX(.9);transform-origin:left}
.detail{font:500 22px/28px Ubuntu,sans-serif;color:var(--ink)}
.email{display:flex;align-items:center;gap:8px;font:500 22px/28px Ubuntu,sans-serif;color:var(--ink)}
.email svg{width:24px;height:17px;flex:none}
.hours{height:66px;background:var(--green);text-align:center;padding-top:9px}
.hours h3{font:600 20px/22px Fredoka,sans-serif;color:var(--highlight)}
.hours p{font:600 20px/24px Fredoka,sans-serif;color:#fff}
</style>
</head>
<body>
<div class="size-label">Size 5.5x8.5 inches</div>
<main class="flyer">
  <header class="header">
    <div class="header-photo" role="img" aria-label="Photo of a medical professional in a surgical cap and mask"></div>
    <div class="brand"><span class="brand-dot"></span><span class="brand-name">CRESTVIEW MEDICAL</span></div>
    <div class="tagline">YOUR HEALTH IS OUR PRIORITY</div>
    <div class="address">42 Harbour Road, Westbay, St. Lorne. Tel : (555) 310 2240 / 2241</div>
  </header>

  <section class="specialties">
    <div class="specialty gp">
      <h2>General<br>Practitioner</h2>
      <div class="phone"><svg viewBox="0 0 16 16"><circle cx="8" cy="8" r="7" fill="none" stroke="#fff" stroke-width="1.5"/><path d="M6 4.5c-1.5 1.5-1.5 5.5 0 7l1.3-1.2-.8-1.3v-2l.8-1.3z" fill="#fff"/></svg>(555) 402 1187</div>
    </div>
    <div class="specialty eye">
      <h2>Ophthalmologist</h2>
      <div class="phone"><svg viewBox="0 0 16 16"><circle cx="8" cy="8" r="7" fill="none" stroke="#fff" stroke-width="1.5"/><path d="M6 4.5c-1.5 1.5-1.5 5.5 0 7l1.3-1.2-.8-1.3v-2l.8-1.3z" fill="#fff"/></svg>(555) 418 3365</div>
    </div>
    <div class="specialty obgyn">
      <h2>Obstetrician/<br>Gynaecologist</h2>
      <div class="phone"><svg viewBox="0 0 16 16"><circle cx="8" cy="8" r="7" fill="none" stroke="#fff" stroke-width="1.5"/><path d="M6 4.5c-1.5 1.5-1.5 5.5 0 7l1.3-1.2-.8-1.3v-2l.8-1.3z" fill="#fff"/></svg><span>(555) 426 7790,<br>(555) 433 9012</span></div>
    </div>
  </section>

  <section class="doctor obgyn">
    <span class="doctor-mark"></span>
    <div class="doctor-info">
      <h1 class="doctor-name">Dr. Selwyn Harcourt</h1>
      <p class="detail">BMedSci, MBBS, DM (O&amp;G), FACOG</p>
      <p class="detail">Obstetrician &amp; Gynaecologist</p>
      <p class="email"><svg viewBox="0 0 24 17"><rect width="24" height="17" fill="#0d3f78"/><path d="M0 0l12 9 12-9M0 17l9-8M24 17l-9-8" stroke="#fff" stroke-width="1.6" fill="none"/></svg>drharcourt@mailbox.com</p>
    </div>
  </section>

  <section class="doctor gp">
    <span class="doctor-mark"></span>
    <div class="doctor-info">
      <h1 class="doctor-name">Dr. Kendrick Barlow</h1>
      <p class="detail">MD, General Practitioner</p>
      <p class="email"><svg viewBox="0 0 24 17"><rect width="24" height="17" fill="#0a72a8"/><path d="M0 0l12 9 12-9M0 17l9-8M24 17l-9-8" stroke="#fff" stroke-width="1.6" fill="none"/></svg>kendrick.barlow.doc@mailbox.com</p>
    </div>
  </section>

  <section class="doctor eye">
    <span class="doctor-mark"></span>
    <div class="doctor-info">
      <p class="service">Clearview Eye Vision Services</p>
      <h1 class="doctor-name">Dr. Lucinda R. Vaskez</h1>
      <p class="detail">MD, Surgeon Ophthalmologist</p>
      <p class="email"><svg viewBox="0 0 24 17"><rect width="24" height="17" fill="#82067f"/><path d="M0 0l12 9 12-9M0 17l9-8M24 17l-9-8" stroke="#fff" stroke-width="1.6" fill="none"/></svg>lucinda.doct@mailnet.com</p>
    </div>
  </section>

  <footer class="hours">
    <h3>OPENING HOURS :</h3>
    <p>Monday - Fridays : 9am - 6pm • &nbsp;Saturdays : 10am - 5pm</p>
  </footer>
</main>
</body>
</html>
```